Flyer-Design für Immobilienmakler
Zielgruppe
Wir sind seit 1992 Immobilienmakler und möchten einen Flyer zur Präsentation unserer Firma und Objektakquise gestalten lassen.
Dieser soll einen Gutschein für eine kostenlose Immobilienbewertung enthalten.
Aufgabenstellung
Wir lassen uns dann überraschen

```html
<!DOCTYPE html>
<html lang="de">
<head>
<meta charset="utf-8">
<title>Flyer Immobilienmakler</title>
<link rel="stylesheet" href="https://fonts.googleapis.com/css2?family=Fira+Sans+Condensed:wght@300;400&family=Fira+Sans+Extra+Condensed:wght@600;700&display=swap">
<style>
:root{
  --beige:#e4dfd9;
  --slate:#c8d0da;
  --white:#ffffff;
  --ink:#1f1f1f;
  --olive:#605f55;
  --grey:#6f7175;
  --rule:#3a3a3a;
}
*{margin:0;padding:0;box-sizing:border-box}
html,body{width:1200px;height:2407px;overflow:hidden;background:var(--white)}
body{position:relative;font-family:"Fira Sans Condensed",sans-serif;color:var(--ink)}
.abs{position:absolute}
.head{font-family:"Fira Sans Extra Condensed",sans-serif;font-weight:700}

/* front side */
.front{left:0;top:0;width:1200px;height:1188px;background:linear-gradient(var(--beige) 0 50%,var(--slate) 50% 100%)}
.front-frame{left:35px;top:28px;width:1131px;height:1125px;border:22px solid var(--white)}
.front-panel{left:156px;top:154px;width:881px;height:880px;background:var(--white);box-shadow:0 0 3px rgba(0,0,0,.15)}
.logo-box{left:228px;top:207px;width:746px;height:128px;border:3px solid var(--olive);border-top:none}
.logo-box-top{top:207px;height:3px;background:var(--olive)}
.firm-name{left:228px;top:186px;width:746px;text-align:center;font-size:72px;line-height:80px;color:#111;letter-spacing:1px}
.firm-rule{left:331px;top:271px;width:532px;height:1px;background:var(--rule)}
.firm-tag{left:228px;top:282px;width:746px;text-align:center;font-family:"Fira Sans Extra Condensed",sans-serif;font-weight:600;font-size:19px}
.street-photo{left:0;top:430px;width:1195px;height:327px;background:linear-gradient(180deg,#d9e3ec 0%,#b9c6d1 35%,#8e8f8c 55%,#a7aba0 70%,#7f9a5c 85%,#9aa59a 100%)}
.front-title{left:156px;top:770px;width:881px;text-align:center;font-weight:300;font-size:54px;letter-spacing:1px}
.front-copy{left:229px;top:834px;width:742px;font-size:31px;line-height:47px;text-align:justify;text-align-last:justify;font-weight:300}
.front-rule{left:228px;top:940px;width:746px;height:2px;background:var(--rule)}
.front-url{left:156px;top:957px;width:881px;text-align:center;font-size:37px;color:var(--olive);font-weight:600}
.social-rule{top:1091px;height:2px;background:var(--white)}
.social{left:492px;top:1074px;width:215px;display:flex;justify-content:center;align-items:center;gap:10px;color:var(--white);font-size:26px}
.social i{display:block;width:24px;height:24px;border:3px solid currentColor;border-radius:5px}

/* back side */
.back{left:0;top:1215px;width:1200px;height:1192px;background:linear-gradient(120deg,#eaeef2,#c9d4df 55%,#e6ebf0)}
.back-scene{left:56px;top:1275px;width:1083px;height:751px;background:linear-gradient(135deg,#f3f0ec 0%,#d7dee6 40%,#b8c6d5 70%,#dfe5ec 100%)}
.back-frame{left:31px;top:1255px;width:1131px;height:1127px;border:22px solid var(--white)}
.back-title{left:60px;top:1316px;width:490px;text-align:center;color:var(--olive);font-size:81px;line-height:86px}
.back-sub{left:60px;top:1400px;width:490px;text-align:center;color:var(--olive);font-size:58px;line-height:62px}
.back-rule{left:136px;width:318px;height:2px;background:var(--rule)}
.back-social{left:136px;top:1518px;width:318px;display:flex;justify-content:center;align-items:center;gap:10px;color:#333;font-size:28px}
.back-social i{display:block;width:30px;height:30px;border:3px solid currentColor;border-radius:6px}
.contact{left:100px;top:1633px;width:390px;text-align:center;font-size:29px;line-height:53px;font-weight:300}
.contact small{font-size:21px}
.back-url{left:100px;top:1910px;width:390px;text-align:center;font-size:30px;font-weight:300}
.team-photo{left:685px;top:1331px;width:419px;height:283px;background:linear-gradient(180deg,#eef0f2 0%,#dfe2e6 45%,#4a4d55 70%,#3a3c42 100%)}
.text-box{left:535px;top:1614px;width:594px;height:412px;background:var(--white)}
.back-head{left:566px;top:1640px;width:524px;font-size:54px;font-weight:300;letter-spacing:1px;text-align:justify;text-align-last:justify}
.back-copy{left:566px;top:1720px;width:524px;font-size:31px;line-height:47.5px;font-weight:300;text-align:justify;text-align-last:justify;letter-spacing:.5px}

/* voucher */
.voucher{left:56px;top:2026px;width:1083px;height:328px;background:var(--slate);border-top:2px dashed var(--white);overflow:hidden}
.voucher-photo{left:0;top:-15px;width:378px;height:378px;border-radius:50%;background:radial-gradient(circle at 45% 55%,#e0b24a 0%,#c9cfd8 25%,#eef1f4 60%,#dfe4ea 100%)}
.voucher-title{left:560px;top:2058px;width:527px;text-align:right;color:var(--white);font-size:92px;line-height:100px;letter-spacing:5px;margin-right:-5px}
.voucher-rule{left:624px;top:2164px;width:515px;height:3px;background:var(--white)}
.voucher-text{left:560px;top:2192px;width:527px;text-align:right;color:var(--grey);font-size:54px;line-height:67px;font-weight:300}
</style>
</head>
<body>
<section class="front abs">
  <div class="front-frame abs"></div>
  <div class="front-panel abs"></div>
  <div class="logo-box abs"></div>
  <div class="logo-box-top abs" style="left:228px;width:98px"></div>
  <div class="logo-box-top abs" style="left:857px;width:117px"></div>
  <div class="firm-name head abs">FIRMENNAME</div>
  <div class="firm-rule abs"></div>
  <div class="firm-tag abs">Lorem ipsum dolor sit amet, consectetuer adipiscing elit, sed diam</div>
  <div class="street-photo abs" role="img" aria-label="Foto einer Neubausiedlung mit Einfamilienhäusern"></div>
  <div class="front-title abs">Lorem ipsum dolor sit</div>
  <p class="front-copy abs">Lorem ipsum dolor sit amet, consectetuer Lorem ipsum dolor sit amet, consectetuer adipiscing elit, sed diam</p>
  <div class="front-rule abs"></div>
  <div class="front-url head abs">www.hausmakler-muster.de</div>
  <div class="social-rule abs" style="left:102px;width:390px"></div>
  <div class="social-rule abs" style="left:707px;width:390px"></div>
  <div class="social abs"><i></i>hausblick</div>
</section>

<section class="back abs"></section>
<div class="back-scene abs" role="img" aria-label="Hintergrundfoto: Hände an einer Tastatur mit Hausmotiven"></div>
<div class="back-frame abs"></div>
<div class="back-title head abs">LOREM IPSUM</div>
<div class="back-sub head abs">DOLOR SIT AMET,</div>
<div class="back-rule abs" style="top:1492px"></div>
<div class="back-social abs"><i></i>hausblick</div>
<div class="contact abs">Firmenanschrift | <small>PLZ ORT</small><br>info@hausmakler-muster.de<br>+49 123 456 78<br>+49 123 456 79</div>
<div class="back-rule abs" style="top:1900px"></div>
<div class="back-url abs">www.hausmakler-muster.de</div>
<div class="team-photo abs" role="img" aria-label="Foto des Maklerteams"></div>
<div class="text-box abs"></div>
<div class="back-head abs">Lorem ipsum dolor sit</div>
<p class="back-copy abs">Lorem ipsum dolor sit amet, consecte-tuer Lorem ipsum dolor sit amet, con-sectetuer adipiscing elit, sed diam no-nummy nibh euismod tincidunt ut laoreet dolore magna aliquam erat vo-lutpat. Ut wisi enim ad minim Lorem</p>

<div class="voucher abs">
  <div class="voucher-photo abs" role="img" aria-label="Foto: Lupe über einem goldenen Haus"></div>
</div>
<div class="voucher-title head abs">GUTSCHEIN</div>
<div class="voucher-rule abs"></div>
<div class="voucher-text abs">für eine kostenlose<br>Immobilienbewertung</div>
</body>
</html>
```